A wedding company selling top 5 wedding venues in an affluent historic Florida Town

We need a word press design (Layered PSD files) to hand over to a web developer.
It's for Maple Hollow Nuptial Company. The company has been set up to sell wedding packages to the top 5 or so wedding venues in Maple Hollow. Maple Hollow is an historic Florida town which is known for it's European village feel, with paved roads and sidewalk seating for cafe's and restaurants.
Needs to be clean and fresh with an elegant feel.
We have a logo already established which you will find attached to the brief along with a few wedding photo's from a couple of the venues we will be selling.
We are starting with 4 venues, which will each have about 3 different packages. I'd like a design for a home page and an inside page.
We will have a blog, recent weddings page which we will update with photo's etc.
The home page will have tabs for:
Wedding Venues, Reception Venues, About US, Contact US, Blog,

Target Market(s)

Brides and Grooms looking for a stylish elegant wedding. Based in western speaking countries, aged between 20 - 50 years old. Probably more aimed at the female who makes the decisions.

Industry/Entity Type

Wedding

Font styles to use
Sans Serif

Colors

Designer to choose colors to be used in the design.

Requirements
Must have
• On the home page I'd like a big slider, A block with a paragraph about Maple Hollow in general, a twitter feed, a recent weddings link and a big button on each page which goes to a "request info" form.

```html
<!DOCTYPE html>
<html lang="en">
<head>
<meta charset="utf-8">
<title>Maple Hollow Nuptial Company</title>
<link rel="stylesheet" href="https://fonts.googleapis.com/css2?family=Ubuntu:wght@400;500;700&family=Open+Sans:wght@400;600&display=swap">
<style>
:root{
  --purple:#a54c9a;
  --purple-dark:#6c3f96;
  --violet:#6b58a3;
  --orange:#f7a24a;
  --ink:#222;
  --grey-text:#555;
  --pale:#ececec;
  --white:#fff;
  --rule:#cfcfcf;
  --fb:#3b5a9a;
  --tw:#2aa9e0;
  --gp:#d9452e;
}
*{box-sizing:border-box;margin:0;padding:0}
html,body{width:1200px;height:2341px;overflow:hidden}
body{position:relative;background:var(--white);font-family:"Open Sans",sans-serif;color:var(--ink)}
.abs{position:absolute}

/* header */
.brand{left:22px;top:52px;font-family:"Ubuntu",sans-serif;font-weight:500;font-size:23px;color:var(--purple-dark);display:flex;align-items:center;gap:10px}
.brand .dot{width:14px;height:14px;border-radius:50%;background:var(--purple)}
.contact{right:214px;top:42px;text-align:right;font-size:13px;color:var(--grey-text);line-height:18px}
.contact strong{font-weight:600;color:#333}
.social{display:flex;gap:3px}
.social span{width:29px;height:29px;display:block}
.social .fb{background:var(--fb)}.social .tw{background:var(--tw)}.social .gp{background:var(--gp)}
.social.top{left:1074px;top:44px}
.nav{left:442px;top:97px;display:flex;gap:24px;font-family:"Ubuntu",sans-serif;font-size:17px;color:var(--purple)}
.request{left:1007px;top:89px;width:160px;height:39px;background:var(--purple-dark);color:var(--white);font-family:"Ubuntu",sans-serif;font-size:19px;display:flex;align-items:center;justify-content:center}

/* hero */
.hero{left:0;top:160px;width:1200px;height:561px;background:linear-gradient(135deg,#3e5a2c 0%,#6f7d4a 35%,#d9d6cf 55%,#f2efe9 70%,#8a5b44 100%)}
.hero-arrow{top:409px;width:67px;height:65px;background:var(--white);display:flex;align-items:center;justify-content:center}
.hero-arrow.prev{left:0}.hero-arrow.next{right:0}
.hero-caption{left:0;top:549px;width:1200px;height:72px;background:rgba(60,60,60,.7);color:var(--white);font-family:"Ubuntu",sans-serif;font-size:33px;display:flex;align-items:center;justify-content:center;padding-right:200px}

/* intro */
.intro-title{left:0;top:746px;width:1200px;text-align:center;font-family:"Ubuntu",sans-serif;font-size:32px;color:var(--purple)}
.intro-copy{left:30px;top:798px;width:1140px;text-align:center;font-size:13.5px;line-height:19px;color:var(--grey-text)}

/* guest */
.guest{left:0;top:883px;width:1200px;height:140px;background:var(--purple)}
.guest-title{left:75px;top:908px;color:var(--white);font-family:"Ubuntu",sans-serif;font-size:33px;line-height:40px}
.guest-title b{font-weight:700}
.guest-label{left:355px;top:922px;color:var(--white);font-size:13px}
.field{top:945px;height:38px;background:var(--white);font-size:12px;color:#666;padding:0 10px;display:flex;align-items:center}
.find{left:937px;top:945px;width:174px;height:38px;background:var(--orange);color:var(--white);font-family:"Ubuntu",sans-serif;font-size:17px;display:flex;align-items:center;justify-content:center}

/* packages */
.packages{left:0;top:1023px;width:1200px;height:441px;background:var(--pale)}
.section-title{left:0;width:1200px;text-align:center;font-family:"Ubuntu",sans-serif;font-size:38px;color:var(--ink)}
.packages-sub{left:0;top:1104px;width:1200px;text-align:center;font-size:17px;line-height:23px;color:#444}
.pkg-box{left:75px;top:1170px;width:1050px;height:235px;background:var(--white);display:flex;box-shadow:0 22px 18px -16px rgba(0,0,0,.25)}
.pkg{flex:1;padding:20px 12px 0 12px;border-left:2px solid #d6d6d6}
.pkg:first-child{border-left:none}
.pkg h3{font-family:"Ubuntu",sans-serif;font-weight:400;font-size:22px;color:var(--violet);margin-bottom:8px}
.pkg p{font-size:11.5px;line-height:17px;color:#555}
.more{display:inline-block;margin-top:14px;width:102px;height:27px;background:var(--violet);color:var(--white);font-size:12px;line-height:27px;text-align:center;border-radius:2px}

/* recent */
.shot{top:1559px;height:280px}
.shot-caption{left:605px;top:1765px;width:281px;height:74px;background:rgba(50,50,50,.72);color:var(--white);font-family:"Ubuntu",sans-serif;font-size:21px;line-height:24px;padding:13px 16px}
.zoom{left:722px;top:1670px;width:44px;height:44px;border-radius:50%;background:rgba(255,255,255,.55)}
.round-arrow{top:1670px;width:32px;height:56px;background:#111;display:flex;align-items:center;justify-content:center}

/* community */
.promo{left:400px;top:1859px;width:800px;height:388px;background:linear-gradient(90deg,#f4f4f4 0%,#9a9a9a 25%,#7c7c7c 60%,#b4b4b4 100%)}
.tweets-icon{left:83px;top:1883px;width:41px;height:41px;background:var(--tw);border-radius:4px}
.tweets-title{left:136px;top:1886px;font-family:"Ubuntu",sans-serif;font-size:28px;color:#333}
.tweet{left:82px;width:318px;padding:6px 2px 8px;border-bottom:2px solid #b9b9b9;font-size:11.5px;line-height:17px;color:#333}
.promo-brand{left:1000px;top:1920px;width:180px;text-align:right;font-family:"Ubuntu",sans-serif;font-weight:500;font-size:20px;line-height:24px;color:var(--purple-dark)}
.promo-title{left:520px;top:1940px;width:590px;text-align:center;font-family:"Ubuntu",sans-serif;font-weight:500;font-size:51px;line-height:52px;color:var(--white)}
.promo-sub{left:503px;top:2082px;width:622px;text-align:center;font-family:"Ubuntu",sans-serif;font-size:22px;color:var(--white);padding-bottom:10px;border-bottom:1px solid rgba(255,255,255,.8)}
.review{left:711px;top:2140px;width:210px;height:40px;background:var(--purple);color:var(--white);font-family:"Ubuntu",sans-serif;font-size:18px;display:flex;align-items:center;justify-content:center}

/* footer */
.foot-nav{left:31px;top:2269px;display:flex;gap:18px;font-size:14px;color:#333}
.copyright{left:31px;top:2294px;font-size:11px;color:#444}
.social.foot{left:1066px;top:2265px}
</style>
</head>
<body>

<header>
  <div class="abs brand"><span class="dot"></span>Maple Hollow Nuptial Company</div>
  <div class="abs contact"><strong>Start Planning Today</strong><br>Call at 000.000.0000 or Email-weddings@maplehollownuptial.com</div>
  <div class="abs social top"><span class="fb"></span><span class="tw"></span><span class="gp"></span></div>
  <nav class="abs nav"><span>Wedding Venues</span><span>Reception Venues</span><span>About Us</span><span>Contact Us</span><span>Blog</span></nav>
  <div class="abs request">Request Info</div>
</header>

<section>
  <div class="abs hero" role="img" aria-label="Bride and groom seated on a garden bench among red roses"></div>
  <div class="abs hero-arrow prev"><svg width="26" height="38" viewBox="0 0 26 38"><path d="M22 4 L5 19 L22 34" fill="none" stroke="#a54c9a" stroke-width="5"/></svg></div>
  <div class="abs hero-arrow next"><svg width="26" height="38" viewBox="0 0 26 38"><path d="M4 4 L21 19 L4 34" fill="none" stroke="#a54c9a" stroke-width="5"/></svg></div>
  <div class="abs hero-caption">“Fast becoming the most popular wedding venue in Central Florida”</div>
</section>

<section>
  <h1 class="abs intro-title">Maple Hollow Wedding Design,Planning, Coordination</h1>
  <p class="abs intro-copy">Want to have a fabulous wedding?&nbsp; You are in luck, we specialize in fabulous weddings! Count on Maple Hollow Nuptial Design to bring your dreams of a beautiful wedding to life.&nbsp; The mission of Maple Hollow Nuptial Design is to alleviate the stress of planning and coordinating a wedding by taking care of everything for you. By paying attention to every detail and always keeping the best interest of the bride and groom in mind we guarantee a flawless wedding day.</p>
</section>

<section>
  <div class="abs guest"></div>
  <div class="abs guest-title">Are you a<br><b>Wedding Guest?</b></div>
  <div class="abs guest-label">Find a couple's wedding website:</div>
  <div class="abs field" style="left:353px;width:281px">First Name</div>
  <div class="abs field" style="left:645px;width:281px">Last Name</div>
  <div class="abs find">Find Coupise</div>
</section>

<section>
  <div class="abs packages"></div>
  <h2 class="abs section-title" style="top:1053px">Wedding Packages</h2>
  <p class="abs packages-sub">If you're looking for a simple no fuss way to organize your Wedding or Quinceañera ceremony<br>and eliminate any worries, why not choose one of our tried and tested packages and leave all the work to us.</p>
  <div class="abs pkg-box">
    <div class="pkg"><h3>Bronze Package</h3><p>Sample text Sample text Sample text Sample text Sample text Sample text Sample text Sample text Sample text Sample text Sample text Sample text Sample text Sample text Sample text Sample text Sample text Sample text Sample text Sample text Sample text</p><span class="more">read more...</span></div>
    <div class="pkg"><h3>Gold Package</h3><p>Sample text Sample text Sample text Sample text Sample text Sample text Sample text Sample text Sample text Sample text Sample text Sample text Sample text Sample text Sample text Sample text Sample text Sample text Sample text Sample text Sample text</p><span class="more">read more...</span></div>
    <div class="pkg"><h3>Platinum Package</h3><p>Sample text Sample text Sample text Sample text Sample text Sample text Sample text Sample text Sample text Sample text Sample text Sample text Sample text Sample text Sample text Sample text Sample text Sample text Sample text Sample text Sample text</p><span class="more">read more...</span></div>
    <div class="pkg"><h3>Quinceañera Package</h3><p>Sample text Sample text Sample text Sample text Sample text Sample text Sample text Sample text Sample text Sample text Sample text Sample text Sample text Sample text Sample text Sample text Sample text Sample text Sample text Sample text Sample text</p><span class="more">read more...</span></div>
  </div>
</section>

<section>
  <h2 class="abs section-title" style="top:1489px">Recent Wedding</h2>
  <div class="abs shot" style="left:70px;width:233px;background:linear-gradient(160deg,#e9e2dc,#8a6a5a 60%,#2b2422)" role="img" aria-label="Couple embracing at their wedding"></div>
  <div class="abs shot" style="left:314px;width:280px;background:linear-gradient(150deg,#c7b39c,#eee9e4 45%,#3a3c44 85%)" role="img" aria-label="Bride with bouquet beside groom in grey suit"></div>
  <div class="abs shot" style="left:605px;width:281px;background:linear-gradient(160deg,#d6d4cf,#9aa48c 40%,#2c2a2c 80%)" role="img" aria-label="Smiling bride and groom outdoors"></div>
  <div class="abs zoom"></div>
  <div class="abs shot-caption">Summer Wedding at<br>Maple Hollow</div>
  <div class="abs shot" style="left:895px;width:235px;background:linear-gradient(160deg,#c9a888,#ece7df 50%,#3a3a3a 90%)" role="img" aria-label="Bride holding pink roses beside a car"></div>
  <div class="abs round-arrow" style="left:70px;border-radius:0 28px 28px 0"><svg width="12" height="16" viewBox="0 0 12 16"><path d="M9 2 L3 8 L9 14" fill="none" stroke="#fff" stroke-width="2.5"/></svg></div>
  <div class="abs round-arrow" style="left:1098px;border-radius:28px 0 0 28px"><svg width="12" height="16" viewBox="0 0 12 16"><path d="M3 2 L9 8 L3 14" fill="none" stroke="#fff" stroke-width="2.5"/></svg></div>
</section>

<section>
  <div class="abs promo" role="img" aria-label="Soft black and white photo of a couple close together"></div>
  <div class="abs tweets-icon"></div>
  <h2 class="abs tweets-title" style="font-weight:400">Our Tweets</h2>
  <p class="abs tweet" style="top:1934px">"This place is beautiful!&nbsp; We thoroughly enjoyed the food, company, scenery and our lovely room. It met our every expectation!"</p>
  <p class="abs tweet" style="top:2009px">"This place is beautiful!&nbsp; We thoroughly enjoyed the food, company, scenery and our lovely room. It met our every expectation!"</p>
  <p class="abs tweet" style="top:2084px">"This place is beautiful!&nbsp; We thoroughly enjoyed the food, company, scenery and our lovely room. It met our every expectation!"</p>
  <p class="abs tweet" style="top:2159px;border-bottom:none">"This place is beautiful!&nbsp; We thoroughly enjoyed the food, company, scenery and our lovely room. It met our every expectation!"</p>
  <div class="abs promo-brand">Maple Hollow Nuptial Company</div>
  <h2 class="abs promo-title">Join the movement to<br>help future couples!</h2>
  <p class="abs promo-sub">Share your vendor reviews and we'll send you a FREE gift</p>
  <div class="abs review">Review Your Vendors</div>
</section>

<footer>
  <nav class="abs foot-nav"><span>Wedding Venues</span><span>Reception Venues</span><span>About Us</span><span>Contact Us</span><span>Blog</span></nav>
  <p class="abs copyright">Copyright Maple Hollow Nuptial Company.</p>
  <div class="abs social foot"><span class="fb"></span><span class="tw"></span><span class="gp"></span></div>
</footer>

</body>
</html>
```